Boutique custom software development company needs new business card

Our nearly 20 year old custom software development company would like to better include the fact that we are now providing Bitcoin services. These new services are B2B include education (how to acquire and securely hold Bitcoin) and integrating Bitcoin payments into existing ecommerce sites or other existing systems. Please keep the card clean and simple. Attached is our current design and some other files. vexalon.example

Target Market(s)

businesses owners interested in long term relationship

Industry/Entity Type

Custom software development and Bitcoin

Contact Information for Business Card

Marcus Ellwood, marcus@vexalon.example, vexalon.example, (888) 555-VEXAL

Font styles to use
Other font styles liked:
• monospace

Requirements
Must have
• double-sided
Nice to have
• clean and simple
Should not have
• physical address

```html
<!DOCTYPE html>
<html lang="en">
<head>
<meta charset="utf-8">
<title>Vexalon Business Card</title>
<link rel="stylesheet" href="https://fonts.googleapis.com/css2?family=Space+Mono:wght@400;700&family=Lato:wght@400&display=swap">
<style>
  :root {
    --stage: #dcdcdc;
    --brand-blue: #2f74c8;
    --deep-blue: #1d4f96;
    --brand-orange: #f47b16;
    --ink: #4a4a4a;
    --paper: #ffffff;
  }
  * { margin: 0; padding: 0; box-sizing: border-box; }
  html, body { width: 1200px; height: 1056px; overflow: hidden; }
  body {
    background: var(--stage);
    display: flex;
    flex-direction: column;
    align-items: center;
    justify-content: center;
    gap: 44px;
  }
  .card {
    width: 760px;
    height: 434px;
    position: relative;
    box-shadow: 0 10px 28px rgba(0,0,0,0.18);
  }

  /* Front */
  .card-front {
    background: var(--brand-blue);
    display: flex;
    flex-direction: column;
    align-items: center;
    justify-content: center;
  }
  .brand-name {
    font-family: "Space Mono", monospace;
    font-weight: 700;
    font-size: 64px;
    letter-spacing: 4px;
    color: var(--paper);
    line-height: 1;
  }
  .brand-tagline {
    margin-top: 14px;
    font-family: "Lato", sans-serif;
    font-size: 24px;
    color: var(--paper);
    letter-spacing: -0.3px;
  }

  /* Back */
  .card-back {
    background: var(--paper);
    display: flex;
    overflow: hidden;
  }
  .card-back::before {
    content: "";
    position: absolute;
    left: 322px;
    top: 0;
    bottom: 0;
    width: 40px;
    background: linear-gradient(90deg, rgba(0,0,0,0.06), rgba(0,0,0,0));
  }
  .brand-block {
    width: 340px;
    display: flex;
    flex-direction: column;
    align-items: center;
    justify-content: center;
    gap: 18px;
  }
  .brand-square {
    width: 190px;
    height: 190px;
    background: var(--brand-blue);
  }
  .brand-web {
    font-family: "Space Mono", monospace;
    font-size: 20px;
    color: var(--brand-blue);
  }
  .contact-block {
    flex: 1;
    padding: 104px 0 0 44px;
    font-family: "Space Mono", monospace;
  }
  .person-name {
    font-size: 32px;
    font-weight: 700;
    letter-spacing: 2px;
    line-height: 1;
  }
  .person-name .first { color: var(--brand-orange); }
  .person-name .last { color: var(--deep-blue); margin-left: 14px; }
  .person-role {
    margin-top: 8px;
    font-size: 17px;
    color: var(--ink);
  }
  .role-rule {
    width: 100px;
    height: 2px;
    background: var(--brand-orange);
    margin: 12px 0 26px;
  }
  .contact-list { list-style: none; }
  .contact-item {
    display: flex;
    align-items: center;
    gap: 12px;
    font-size: 17px;
    color: var(--ink);
    margin-bottom: 14px;
  }
  .contact-icon {
    width: 28px;
    height: 28px;
    border-radius: 4px;
    background: var(--brand-blue);
    display: flex;
    align-items: center;
    justify-content: center;
    flex-shrink: 0;
  }
  .contact-icon svg { width: 18px; height: 18px; }
</style>
</head>
<body>
  <section class="card card-front">
    <div class="brand-name">VEXALON</div>
    <div class="brand-tagline">developer of custom applications</div>
  </section>

  <section class="card card-back">
    <div class="brand-block">
      <div class="brand-square"></div>
      <div class="brand-web">vexalon.example</div>
    </div>
    <div class="contact-block">
      <div class="person-name"><span class="first">MARCUS</span><span class="last">ELLWOOD</span></div>
      <div class="person-role">Software Developer</div>
      <div class="role-rule"></div>
      <ul class="contact-list">
        <li class="contact-item">
          <span class="contact-icon">
            <svg viewBox="0 0 24 24"><path fill="#fff" d="M6.6 10.8c1.4 2.8 3.8 5.1 6.6 6.6l2.2-2.2c.3-.3.7-.4 1-.2 1.1.4 2.3.6 3.6.6.6 0 1 .4 1 1V20c0 .6-.4 1-1 1C10.6 21 3 13.4 3 4c0-.6.4-1 1-1h3.5c.6 0 1 .4 1 1 0 1.3.2 2.5.6 3.6.1.3 0 .7-.2 1l-2.3 2.2z"/></svg>
          </span>
          (888) 555-VEXAL
        </li>
        <li class="contact-item">
          <span class="contact-icon">
            <svg viewBox="0 0 24 24"><rect x="3" y="5" width="18" height="14" fill="none" stroke="#fff" stroke-width="2"/><path d="M3 5l9 8 9-8M3 19l7-7M21 19l-7-7" fill="none" stroke="#fff" stroke-width="2"/></svg>
          </span>
          marcus@vexalon.example
        </li>
        <li class="contact-item">
          <span class="contact-icon">
            <svg viewBox="0 0 24 24"><path fill="#fff" d="M6 3l13 10h-6l3.5 7-2.5 1.2L10.6 14 6 18z"/></svg>
          </span>
          vexalon.example
        </li>
      </ul>
    </div>
  </section>
</body>
</html>
```